I need a label with logo to go on jars of honey.
Label size 70mm x 70mm
The front label should say :
The Tall Fern Honey Co. (logo)
Tarepo Honey
400g
The back label:
Would have nutritional information
And our address
You can see from the uploaded files the styles I prefer, I have uploaded a photo of the honey product too. The background of the logo doesn't have to be white. I would like to develop a color scheme that would look nice against the color of the honey.
Logo Text
The Tall Fern Honey Co. / The Tall Fern Honey Company

```html
<!DOCTYPE html>
<html lang="en">
<head>
<meta charset="utf-8">
<title>The Tall Fern Honey Co. – Jar Labels</title>
<link rel="stylesheet" href="https://fonts.googleapis.com/css2?family=Copse&family=Bree+Serif&family=Marcellus&display=swap">
<style>
  :root {
    --stage: #0c0002;
    --label-warm: #ffe451;
    --label-mid: #ffd978;
    --label-pale: #fff0a8;
    --comb-light: #ffb13a;
    --comb-deep: #f07d12;
    --brand-orange: #f07a12;
    --ink: #1e0a04;
    --rule-grey: #a89a74;
    --rule-dot: #b9a77a;
  }
  * { box-sizing: border-box; margin: 0; padding: 0; }
  html, body { width: 1200px; height: 1018px; overflow: hidden; background: var(--stage); }
  .canvas { position: relative; width: 1200px; height: 1018px; background: var(--stage); }

  .label {
    position: absolute;
    width: 506px; height: 506px;
    background: linear-gradient(90deg, var(--label-warm) 0%, var(--label-mid) 40%, var(--label-pale) 100%);
    overflow: hidden;
    font-family: "Copse", serif;
    color: var(--ink);
  }
  .label--back { left: 73px; top: 279px; }
  .label--front { left: 621px; top: 265px; }

  .comb-band {
    position: absolute; left: 0; top: 0; width: 100%; height: 33px;
    background: linear-gradient(180deg, var(--comb-light), var(--comb-deep));
  }
  .comb-base { position: absolute; left: 0; bottom: 0; width: 506px; height: 140px; }

  /* Back label */
  .nutrition-title {
    position: absolute; left: 126px; top: 52px;
    font-family: "Bree Serif", serif; font-size: 34px; line-height: 1; letter-spacing: 1px;
  }
  .serving-line {
    position: absolute; left: 131px; top: 85px;
    font-family: "Bree Serif", serif; font-size: 11px; letter-spacing: 1px; word-spacing: 2px; white-space: nowrap;
  }
  .title-rule { position: absolute; left: 128px; top: 124px; width: 255px; height: 4px; background: var(--brand-orange); }

  .nutrition-table { position: absolute; left: 128px; top: 140px; width: 300px; font-size: 13px; letter-spacing: 0.4px; }
  .nutrition-table .head { position: relative; height: 78px; }
  .nutrition-table .head span { position: absolute; white-space: nowrap; }
  .head .rule { position: absolute; left: 0; width: 255px; height: 1px; background: var(--rule-grey); }
  .nutrition-table .row {
    display: grid; grid-template-columns: 116px 106px auto;
    width: 255px; height: 21.5px; line-height: 21px;
    border-bottom: 1px dotted var(--rule-dot);
    white-space: nowrap;
  }

  /* Front label */
  .brand-name {
    position: absolute; left: 120px; top: 90px;
    font-size: 24px; line-height: 1.1; color: var(--brand-orange); text-align: center;
    width: 230px;
  }
  .brand-dot {
    position: absolute; left: 330px; top: 68px; width: 26px; height: 26px;
    border-radius: 50%; background: var(--brand-orange);
  }
  .product-name {
    position: absolute; left: 167px; top: 190px;
    font-family: "Marcellus", serif; font-size: 55px; line-height: 58px; color: var(--ink);
  }
  .tagline {
    position: absolute; left: 0; width: 512px; top: 351px; text-align: center;
    font-size: 17px; letter-spacing: 0.3px;
  }
  .weight { position: absolute; left: 0; width: 512px; top: 390px; text-align: center; font-size: 17px; }

  .dipper-art {
    position: absolute; left: 0; top: 228px; width: 103px; height: 168px;
    background: radial-gradient(ellipse at 60% 40%, #ffce3d, #f3a51a 60%, rgba(240,160,20,0) 75%);
  }
  .honeycomb-art {
    position: absolute; left: 360px; top: 358px; width: 146px; height: 148px;
    background: radial-gradient(ellipse at 70% 45%, #ffd94a, #f5b324 55%, #e9951a);
    clip-path: polygon(52% 0, 100% 0, 100% 100%, 0 100%, 0 42%, 50% 27%);
  }
</style>
</head>
<body>
<main class="canvas">

  <section class="label label--back" aria-label="Back label">
    <div class="comb-band" role="img" aria-label="Honeycomb border pattern"></div>

    <h1 class="nutrition-title">Nutrition Facts</h1>
    <p class="serving-line">Serving Per Package: 25 &nbsp;&nbsp;Serving Size: 20g</p>
    <div class="title-rule"></div>

    <div class="nutrition-table">
      <div class="head">
        <span style="left:116px;top:0">Average</span>
        <span style="left:222px;top:0">Average</span>
        <div class="rule" style="top:18px"></div>
        <span style="left:116px;top:21px">Quantity</span>
        <span style="left:222px;top:21px">Quantity Per</span>
        <div class="rule" style="top:38px"></div>
        <span style="left:116px;top:43px">Per Serving</span>
        <span style="left:222px;top:43px">100 g</span>
      </div>
      <div class="row"><span>Energy</span><span>272kj</span><span>1360 kj</span></div>
      <div class="row"><span>Protein</span><span>0.08g</span><span>0.4 g</span></div>
      <div class="row"><span>Fat, total</span><span>0g</span><span>0g</span></div>
      <div class="row"><span>Saturated</span><span>0g</span><span>0g</span></div>
      <div class="row"><span>Carbohydrated</span><span>15.9 g</span><span>79.6g</span></div>
      <div class="row"><span>Sugars</span><span>15.6 g</span><span>78.1g</span></div>
      <div class="row"><span>Sodium</span><span>2.4 mg</span><span>12 mg</span></div>
    </div>

    <svg class="comb-base" viewBox="0 0 506 140" role="img" aria-label="Honeycomb pattern rising from the bottom edge">
      <defs>
        <linearGradient id="combBack" x1="0" y1="0" x2="0" y2="1">
          <stop offset="0" stop-color="#ffb13a"/><stop offset="1" stop-color="#f07d12"/>
        </linearGradient>
      </defs>
      <path fill="url(#combBack)" d="M0 0 H30 V27 H75 V53 H170 V80 H185 V53 H275 V80 H305 V53 H400 V27 H490 V53 H506 V140 H0 Z"/>
    </svg>
  </section>

  <section class="label label--front" aria-label="Front label">
    <div class="comb-band" role="img" aria-label="Honeycomb border pattern"></div>

    <p class="brand-name">The Tall Fern<br>Honey Co.</p>
    <span class="brand-dot"></span>

    <h2 class="product-name">Tarepo<br>Honey</h2>

    <p class="tagline">100% Pure Law Organic Honey</p>
    <p class="weight">400g</p>

    <svg class="comb-base" viewBox="0 0 506 140" role="img" aria-label="Honeycomb pattern rising from the bottom edge">
      <defs>
        <linearGradient id="combFront" x1="0" y1="0" x2="0" y2="1">
          <stop offset="0" stop-color="#ffb13a"/><stop offset="1" stop-color="#f07d12"/>
        </linearGradient>
      </defs>
      <path fill="url(#combFront)" d="M0 0 H30 V28 H85 V55 H135 V28 H165 V55 H290 V80 H310 V55 H370 V140 H0 Z M0 55 H506 V140 H0 Z"/>
    </svg>

    <div class="dipper-art" role="img" aria-label="Illustration of a honey dipper dripping honey with a bee"></div>
    <div class="honeycomb-art" role="img" aria-label="Photograph of honeycomb pieces"></div>
  </section>

</main>
</body>
</html>
```